Bold Meridian Businesses Flyers

Needing to put together three flyers (one we will want to have printed front and back) for our industrial contracting services, our scaffolding business and then our fabrication business. I have found a sample design and come up with some replacement verbiage but need help putting it together. Attached is the sample flyer in blue and then a couple of our current flyers that we will want to convert to a format like the sample flyer. I have logos, colors, etc. that I can upload we will also need to come up with some pictures

Designers have requested I extend this

```html
<!DOCTYPE html>
<html lang="en">
<head>
<meta charset="utf-8">
<title>Bold Meridian Scaffolding Flyer</title>
<link rel="stylesheet" href="https://fonts.googleapis.com/css2?family=Bebas+Neue&family=Oswald:wght@500;700&family=Montserrat:wght@400;500;700&display=swap">
<style>
:root{
  --red:#e31e26;
  --red-deep:#b8121a;
  --ink:#111111;
  --white:#ffffff;
  --stage:#e8e8e9;
  --grey:#8a8a8c;
  --rule:#2a2a2a;
}
*{margin:0;padding:0;box-sizing:border-box}
html,body{width:1200px;height:731px;overflow:hidden;background:var(--stage)}
.flyer{position:absolute;left:170px;top:59px;width:860px;height:613px;overflow:hidden;
  background:linear-gradient(180deg,#f6f6f7 0%,#e6e6e8 75%,#cfcfd2 100%);
  box-shadow:0 6px 16px rgba(0,0,0,.18);font-family:"Montserrat",sans-serif;color:var(--ink)}
.photo-workshop{position:absolute;left:0;top:0;width:560px;height:380px;
  background:linear-gradient(120deg,#e9eef1 0%,#c8cdd1 40%,#6d6a68 58%,#d2542c 70%,#ece9e4 100%)}
.photo-plant{position:absolute;left:0;top:0;width:860px;height:470px;
  background:linear-gradient(135deg,#d9d9db 0%,#f4f4f5 45%,#e2e2e4 70%,#c9c9cc 100%);
  clip-path:path("M536,0 L860,0 L860,428 C700,440 520,455 404,467 C380,400 340,340 312,311 C330,200 420,80 536,0 Z")}
.plant-fade{position:absolute;left:380px;top:160px;width:480px;height:300px;
  background:radial-gradient(ellipse at 40% 50%,rgba(255,255,255,.85),rgba(255,255,255,0) 70%)}
.shapes{position:absolute;left:0;top:0}
.photo-inspector{position:absolute;left:722px;top:300px;width:138px;height:313px;
  background:linear-gradient(180deg,#2b4a8c 0%,#2b4a8c 8%,#e9e1d6 14%,#dfe44a 30%,#f2f2ee 45%,#c9a77e 70%,#b08a5f 100%);
  border-radius:40px 0 0 0}
.brand{position:absolute;left:606px;top:72px;width:226px;text-align:center}
.brand-name{display:flex;align-items:center;justify-content:center;gap:7px;
  font:700 16px/1 "Montserrat",sans-serif;color:var(--red);letter-spacing:1.5px;text-transform:uppercase}
.brand-name i{width:11px;height:11px;border-radius:50%;background:var(--red);display:block}
.brand-line{font:500 15px/1 "Montserrat",sans-serif;color:var(--grey);margin-top:8px;letter-spacing:.5px}
.headline-top{position:absolute;left:451px;top:132px;font:700 34px/1 "Oswald",sans-serif;font-style:italic;letter-spacing:-1px;color:var(--ink)}
.headline-main{position:absolute;left:388px;top:158px;font:700 76px/1 "Oswald",sans-serif;font-style:italic;letter-spacing:-2px;color:var(--red);
  text-shadow:0 2px 2px rgba(0,0,0,.2)}
.feature{position:absolute;left:452px;font:500 8.8px/10.7px "Montserrat",sans-serif;text-align:justify;text-align-last:left;color:var(--ink)}
.f1{top:250px;width:300px}
.f2{top:306px;width:300px}
.f3{top:361px;width:231px}
.feature-rule{position:absolute;left:452px;width:302px;height:1px;background:var(--rule)}
.badge{position:absolute;left:391px;width:46px;height:46px;border-radius:50%;background:var(--red);
  border:2px solid #fff;box-shadow:0 0 0 1.5px var(--red-deep),0 2px 4px rgba(0,0,0,.25);display:flex;align-items:center;justify-content:center;color:#fff}
.b1{top:246px}.b2{top:302px}.b3{top:363px}
.badge svg{width:22px;height:22px}
.provide{position:absolute;left:38px;top:340px;font:700 31px/1 "Oswald",sans-serif;font-style:italic;color:#fff;letter-spacing:-1px}
.solutions{position:absolute;left:27px;top:373px;font:700 44px/1 "Oswald",sans-serif;color:#ececec;letter-spacing:-2px;text-shadow:0 2px 3px rgba(0,0,0,.3)}
.solutions-rule{position:absolute;left:25px;top:429px;width:315px;height:1.5px;background:#fff}
.service{position:absolute;color:#fff;font:400 11.5px/13px "Montserrat",sans-serif;white-space:nowrap}
.service small{display:block;font:400 7.8px/10px "Montserrat",sans-serif;margin-top:1px}
.svc-icon{position:absolute;width:26px;height:26px;color:#fff}
.svc-rule{position:absolute;width:135px;height:1px;background:rgba(255,255,255,.8)}
.call-row{position:absolute;left:446px;top:500px;display:flex;align-items:center;gap:14px}
.call{font:400 33px/1 "Bebas Neue",sans-serif;color:var(--ink)}
.call-badge{width:48px;height:48px;border-radius:50%;background:var(--red);flex:none;
  border:2px solid #fff;box-shadow:0 0 0 1.5px var(--red-deep);display:flex;align-items:center;justify-content:center}
.phone{font:400 35px/1 "Bebas Neue",sans-serif;color:var(--ink);margin-left:3px}
.contact-row{position:absolute;left:444px;top:563px;display:flex;align-items:center;gap:10px}
.contact{font:400 16px/13px "Bebas Neue",sans-serif;color:var(--ink);display:flex;align-items:center;gap:7px;white-space:nowrap}
.mini-badge{width:23px;height:23px;border-radius:50%;border:1.5px solid var(--red);display:flex;align-items:center;justify-content:center;flex:none}
.mini-badge span{width:15px;height:15px;border-radius:50%;background:var(--red);display:flex;align-items:center;justify-content:center}
</style>
</head>
<body>
<main class="flyer">
  <div class="photo-workshop" role="img" aria-label="Technician in safety glasses operating an orange industrial lift in a workshop"></div>
  <div class="photo-plant" role="img" aria-label="Faded industrial plant piping and steel structure"></div>
  <div class="plant-fade"></div>

  <svg class="shapes" width="860" height="613" viewBox="0 0 860 613" aria-hidden="true">
    <defs>
      <radialGradient id="panelRed" cx="35%" cy="30%" r="80%">
        <stop offset="0" stop-color="#f0262e"/><stop offset="1" stop-color="#d7141c"/>
      </radialGradient>
      <linearGradient id="sweep" x1="0" y1="0" x2="1" y2="0">
        <stop offset="0" stop-color="#c8141c"/><stop offset="1" stop-color="#ee2a31"/>
      </linearGradient>
    </defs>
    <path d="M545,-4 C430,70 335,190 300,320" fill="none" stroke="#fff" stroke-width="26"/>
    <path d="M545,-4 C430,70 335,190 300,320" fill="none" stroke="url(#sweep)" stroke-width="11"/>
    <path d="M404,480 C560,462 720,445 860,428 L860,613 L390,613 Z" fill="#e4e4e6"/>
    <path d="M404,470 C560,454 720,436 860,420" fill="none" stroke="url(#sweep)" stroke-width="14"/>
    <path d="M404,482 C560,466 720,448 860,432" fill="none" stroke="#fff" stroke-width="4"/>
    <path d="M0,613 L0,335 C70,282 150,268 215,274 C330,286 410,370 420,470 C426,530 414,580 402,613 Z" fill="#d9d9db"/>
    <path d="M0,613 L0,355 C60,300 140,285 200,290 C300,300 382,380 394,470 C400,530 388,580 378,613 Z" fill="url(#panelRed)"/>
  </svg>

  <div class="photo-inspector" role="img" aria-label="Site supervisor in hard hat and hi-vis vest holding rolled plans"></div>

  <div class="brand">
    <div class="brand-name"><i></i>Bold Meridian</div>
    <div class="brand-line">Scaffolding</div>
  </div>

  <div class="headline-top">Engineered to</div>
  <div class="headline-main">Outperform</div>

  <div class="badge b1"><svg viewBox="0 0 24 24" fill="none" stroke="#fff" stroke-width="1.8"><circle cx="12" cy="12" r="9.5" stroke-dasharray="44 6"/><text x="12" y="15.5" text-anchor="middle" font-family="Montserrat" font-size="8.5" font-weight="700" fill="#fff" stroke="none">24</text></svg></div>
  <div class="badge b2"><svg viewBox="0 0 24 24" fill="#fff"><circle cx="11" cy="7" r="4"/><path d="M3 21c0-5 3.5-8 8-8s8 3 8 8z"/></svg></div>
  <div class="badge b3"><svg viewBox="0 0 24 24" fill="none" stroke="#fff" stroke-width="2.4" stroke-linecap="round"><path d="M5 5l14 14"/><circle cx="5" cy="5" r="2.5"/><path d="M15 19l4-4"/></svg></div>

  <p class="feature f1">Our team responds to your needs quickly and works with responsibility and discipline, performing maintenance, installation, adjustment, or repair of your equipment 24/7, ensuring your company remains productive and efficient every hour of operation.</p>
  <div class="feature-rule" style="top:292px"></div>
  <p class="feature f2">Welders, millwrights, mechanics, carpenters, ready to support your operation. We attend professionally manufacturing areas of carbon steel, stainless steel, structural steel, sheet metal, aluminum and chromium alloy.</p>
  <div class="feature-rule" style="top:352px"></div>
  <p class="feature f3">Our machinists and mechanics move, assemble and install the machinery in a safe way, taking special care with the exact positioning and rigging. They also dismantle, move and check equipment and machinery.</p>

  <div class="provide">PROVIDING</div>
  <div class="solutions">SOLUTIONS FOR</div>
  <div class="solutions-rule"></div>

  <svg class="svc-icon" style="left:24px;top:447px" viewBox="0 0 26 26" fill="#fff"><rect x="3" y="12" width="20" height="12"/><rect x="5" y="4" width="3" height="8"/><rect x="10" y="7" width="3" height="5"/></svg>
  <div class="service" style="left:57px;top:458px">Shutdowns &amp; overhauls</div>
  <div class="svc-rule" style="left:57px;top:475px"></div>

  <svg class="svc-icon" style="left:24px;top:485px" viewBox="0 0 26 26" fill="#fff"><circle cx="10" cy="11" r="6"/><circle cx="20" cy="20" r="4"/></svg>
  <div class="service" style="left:57px;top:481px">Mechanical systems<small>Installation, inspection &amp; repair</small></div>
  <div class="svc-rule" style="left:57px;top:513px"></div>

  <svg class="svc-icon" style="left:24px;top:521px" viewBox="0 0 26 26" fill="none" stroke="#fff" stroke-width="2"><path d="M4 24h14M11 24V14l8-8M19 6l4 2"/><circle cx="11" cy="14" r="2.5"/></svg>
  <div class="service" style="left:57px;top:519px">Fabrication and Custom<br>Design</div>
  <div class="svc-rule" style="left:57px;top:552px"></div>

  <svg class="svc-icon" style="left:24px;top:560px" viewBox="0 0 26 26" fill="#fff"><rect x="2" y="14" width="14" height="10"/><path d="M18 24l3-16 3 16z"/></svg>
  <div class="service" style="left:57px;top:561px">Power plant equipment<small>Installation, inspection &amp; repair</small></div>

  <svg class="svc-icon" style="left:206px;top:451px" viewBox="0 0 26 26" fill="#fff"><rect x="8" y="6" width="10" height="14"/><path d="M1 13l5-4v8zM25 13l-5-4v8z"/></svg>
  <div class="service" style="left:241px;top:457px">Pressure Vessel<small>Installation &amp; repair</small></div>
  <div class="svc-rule" style="left:241px;top:487px"></div>

  <svg class="svc-icon" style="left:206px;top:482px" viewBox="0 0 26 26" fill="#fff"><rect x="11" y="2" width="5" height="12"/><rect x="3" y="14" width="20" height="6"/><rect x="1" y="13" width="2" height="8"/><rect x="23" y="13" width="2" height="8"/></svg>
  <div class="service" style="left:241px;top:489px">Process piping<small>Installation &amp; repair</small></div>
  <div class="svc-rule" style="left:241px;top:518px"></div>

  <svg class="svc-icon" style="left:206px;top:522px" viewBox="0 0 26 26" fill="none" stroke="#fff" stroke-width="2.4" stroke-linecap="round"><path d="M4 4l16 16"/><circle cx="5" cy="5" r="3"/><path d="M14 22l8-8"/></svg>
  <div class="service" style="left:241px;top:522px">General plant &amp; facility<br>Maintenance</div>

  <div class="call-row">
    <div class="call">CALL US</div>
    <div class="call-badge"><svg width="24" height="24" viewBox="0 0 24 24" fill="#fff"><path d="M6.6 10.8a15 15 0 0 0 6.6 6.6l2.2-2.2c.3-.3.7-.4 1-.2 1.1.4 2.3.6 3.6.6.6 0 1 .4 1 1V20c0 .6-.4 1-1 1A17 17 0 0 1 3 4c0-.6.4-1 1-1h3.5c.6 0 1 .4 1 1 0 1.3.2 2.5.6 3.6.1.3 0 .7-.2 1z"/></svg></div>
    <div class="phone">307.555.0148</div>
  </div>

  <div class="contact-row">
    <div class="contact"><div class="mini-badge"><span><svg width="9" height="9" viewBox="0 0 10 10" fill="none" stroke="#fff" stroke-width="1"><circle cx="5" cy="5" r="4"/><path d="M1 5h8M5 1c2 2 2 6 0 8M5 1c-2 2-2 6 0 8"/></svg></span></div>BM-FIELDWORKS.COM</div>
    <div class="contact"><div class="mini-badge"><span><svg width="8" height="10" viewBox="0 0 8 10" fill="#fff"><path d="M4 0a4 4 0 0 1 4 4c0 3-4 6-4 6S0 7 0 4a4 4 0 0 1 4-4z"/></svg></span></div><span>880 COMMERCE LOOP MESA FALLS,<br>WY 82099</span></div>
  </div>
</main>
</body>
</html>
```